Refresh Old Magazine Ads - II

Hi. I would like to refresh the following magazine ads. The size of both ads are as follows:
MRQ Ad
51 x 66 picas (full bleed)	8 1/2” x 11” (full bleed)
49 x 64 picas (trimmed)	8 1/8" x 10 5/8" (trimmed)
French ½ Page Ad
Half page, horizontal 		41p8 x 27 picas 7” x 4 1/2"
I want both source files in Photoshop editable files.
1. For the first MRQ Ad, see attached folder in the link with accompanying docs. Use the wording found in the document called “2023 MRQ Canada AD”. If you want more info, you can check the website at meadowreadingquest.com.
Also, you will notice that I have a new logo. I want the eps pic of the open book to be included in the photoshop file of the logo so that the end results looks like the document called “What I Want NEW MRQ Logo to look like”.
2. The second ad is to advertise our VESK store with some French products. See attached folder called “French ½ page ad” which includes old ad. Use the same wording as old ad. Please nothing with yoga or people with jewelry.
I would also prefer that the ads NOT be dark but more towards the brighter/lighter side.
LINK FOR ALL FILES: https://www.boxvaultshare.com/s/qk3r8tz5m1wpa7/Files%20for%20Ad%20Designs.zip?dl=0

```html
<!DOCTYPE html>
<html lang="fr">
<head>
<meta charset="utf-8">
<title>Cette année, offrez le don de la santé – annonce demi-page</title>
<link rel="stylesheet" href="https://fonts.googleapis.com/css2?family=Roboto:wght@300;400;700&display=swap">
<style>
  :root {
    --canvas-bg: #e9e9e9;
    --banner-red: #7e1616;
    --banner-red-deep: #5e0d0d;
    --text-dark: #222222;
    --text-light: #ffffff;
    --cream: #efe6d6;
    --sand: #d9c7a6;
    --sun: #f1c865;
    --leaf: #6f8a3a;
    --leaf-deep: #3f5a22;
    --icon-ring: #9a9a9a;
  }
  * { box-sizing: border-box; margin: 0; padding: 0; }
  html, body {
    width: 900px; height: 1200px; overflow: hidden;
    background: var(--canvas-bg);
    font-family: "Roboto", Arial, sans-serif;
  }
  .canvas { position: relative; width: 900px; height: 1200px; }

  .ad {
    position: absolute; left: 20px; top: 355px;
    width: 860px; height: 490px; overflow: hidden;
    box-shadow: 0 6px 18px rgba(0,0,0,0.25);
  }
  .ad-photo {
    position: absolute; inset: 0;
    background:
      radial-gradient(ellipse 40% 55% at 78% 62%, rgba(120,150,70,0.9), transparent 70%),
      linear-gradient(90deg, var(--cream) 0%, #ead9b9 28%, var(--sun) 48%, var(--leaf) 66%, var(--leaf-deep) 85%, #7d9a4a 100%);
  }
  .ad-photo::after {
    content: ""; position: absolute; left: 0; right: 0; bottom: 0; height: 35%;
    background: linear-gradient(0deg, rgba(217,199,166,0.9), transparent);
  }

  .headline-band {
    position: absolute; left: 0; top: 17px; width: 500px; height: 122px;
    background: linear-gradient(90deg, var(--banner-red) 0%, var(--banner-red) 70%, rgba(126,22,22,0) 100%);
    color: var(--text-light);
    padding: 10px 0 0 28px;
  }
  .headline {
    font-weight: 400; font-size: 34px; line-height: 40px; letter-spacing: 0.2px;
    text-shadow: 0 1px 2px rgba(0,0,0,0.35);
  }
  .subhead { font-weight: 300; font-size: 19px; line-height: 24px; margin-top: 2px; }

  .points { list-style: none; }
  .point {
    position: absolute; left: 0;
    font-size: 16.5px; line-height: 22px; color: var(--text-dark);
    padding-left: 51px;
  }
  .point-marker {
    position: absolute; left: 0; top: 2px; width: 42px; height: 22px;
  }
  .point-1 { top: 160px; width: 420px; }
  .point-2 { top: 291px; width: 330px; }
  .point-3 { top: 400px; width: 330px; }
  .point strong { font-weight: 700; }

  .product {
    position: absolute;
    box-shadow: 2px 3px 8px rgba(0,0,0,0.35);
  }
  .product-magazine {
    left: 332px; top: 282px; width: 131px; height: 206px;
    background: linear-gradient(180deg, #1f5fbf 0%, #3aa0e0 45%, #8cc63f 100%);
  }
  .product-wallet {
    left: 448px; top: 352px; width: 88px; height: 131px;
    background: linear-gradient(180deg, #3a3a3a, #1e1e1e);
  }
  .product-booklet {
    left: 540px; top: 395px; width: 122px; height: 80px;
    background: linear-gradient(90deg, #f4f1e6 0%, #ffffff 48%, #f0f0e8 52%, #8cc63f 100%);
    transform: skewX(-14deg) rotate(-8deg);
  }
</style>
</head>
<body>
<main class="canvas">
  <section class="ad">
    <div class="ad-photo" role="img" aria-label="Photo d'une mère et de sa fille souriantes courant sur un sentier ensoleillé bordé d'arbres verts"></div>

    <header class="headline-band">
      <h1 class="headline">CETTE ANNÉE, OFFREZ<br>LE DON DE LA SANTÉ!</h1>
      <p class="subhead">Un moyen abordable de partager votre foi</p>
    </header>

    <ul class="points">
      <li class="point point-1">
        <svg class="point-marker" viewBox="0 0 42 22" aria-hidden="true">
          <rect x="0" y="7" width="22" height="8" fill="var(--banner-red)"/>
          <circle cx="30" cy="11" r="10" fill="#fff" stroke="var(--icon-ring)" stroke-width="1.2"/>
          <rect x="24" y="7.5" width="12" height="7" rx="1.5" fill="none" stroke="#666" stroke-width="1.1"/>
          <circle cx="33" cy="11" r="1.1" fill="#666"/>
        </svg>
        Le magazine et le portefeuille santé font de merveilleux cadeaux pour les occasions spéciales, les séries d'évangélisation, les kiosques, et même pour la distribution de porte-à-porte. Le portefeuille contient trois tracts.
      </li>
      <li class="point point-2">
        <svg class="point-marker" viewBox="0 0 42 22" aria-hidden="true">
          <rect x="0" y="7" width="22" height="8" fill="var(--banner-red)"/>
          <circle cx="30" cy="11" r="10" fill="#fff" stroke="var(--icon-ring)" stroke-width="1.2"/>
          <rect x="24.5" y="6" width="11" height="8" rx="1" fill="none" stroke="#666" stroke-width="1.1"/>
          <line x1="28" y1="16.5" x2="32" y2="16.5" stroke="#666" stroke-width="1.1"/>
        </svg>
        Ces ressources peuvent être données aux croyants comme aux personnes qui n’ont aucun intérêt spirituel.
      </li>
      <li class="point point-3">
        <svg class="point-marker" viewBox="0 0 42 22" aria-hidden="true">
          <rect x="0" y="7" width="22" height="8" fill="var(--banner-red)"/>
          <circle cx="30" cy="11" r="10" fill="#fff" stroke="var(--icon-ring)" stroke-width="1.2"/>
          <circle cx="30" cy="9" r="3" fill="none" stroke="#666" stroke-width="1.1"/>
          <path d="M25 16.5 Q30 12 35 16.5" fill="none" stroke="#666" stroke-width="1.1"/>
        </svg>
        Contactez la Librairie Horizon pour faire votre commande ou visitez <strong>veskcanada.ca/store</strong>
      </li>
    </ul>

    <div class="product product-magazine" role="img" aria-label="Couverture du magazine santé avec un grand chiffre 8 illustré de fruits et de scènes de bien-être"></div>
    <div class="product product-wallet" role="img" aria-label="Portefeuille santé noir avec titre lettré à la main et trois petites vignettes"></div>
    <div class="product product-booklet" role="img" aria-label="Tract santé ouvert montrant du texte et des photos"></div>
  </section>
</main>
</body>
</html>
```